Attention Getting Doorhanger Postcard Campaign offering HUGE Rebate on New Construction Homes

I am reestablishing my real estate career in the far North Dallas, TX area and want to offer a rebate on new construction homes to help get me started. I am requesting a doorhanger as my first project but would like a theme that I can carry over to other projects including postcards and other marketing items. I want it to look high end, clean, professional and classy. I am attaching a copy of a flier that I created that needs (no graphic designer here) some prettying up. But this is just to give you an idea of the type of style that is of interest to me.

Target Market(s)

Home buyers for new construction in far north dallas suburbs. Usually a move up buyer.

Industry/Entity Type

Real Estate

Colors

Designer to choose colors to be used in the design.

Requirements
Must have
• Catch phrase, draw attention, classy clean lines, current trend colors of blues and grays. My information, Marston Pryce logo, equal housing and realtor logos. Fine Print: Not intended to solicit homes already listed for sale or buyers already in a buyers agency agreement with another brokerage. Please include offer details as listed in my flier. Again I am interested in a door hanger and the next round would be a flier or postcard.
Nice to have
• Picture of new homes that are in line with what is being built in my area. A few home builders sites: Coastal Beacon, Riverbend Homes, Fenwick Homes, Calloway Homes.

```html
<!DOCTYPE html>
<html lang="en">
<head>
<meta charset="utf-8">
<title>Door Hanger – New Construction Rebate</title>
<link href="https://fonts.googleapis.com/css2?family=Montserrat:wght@500;600;700;800&family=Roboto:ital,wght@0,400;0,500;0,700;1,400&family=Great+Vibes&display=swap" rel="stylesheet">
<style>
  :root{
    --page:#e6e9ee;
    --blue:#0a5cc0;
    --blue-deep:#06449a;
    --blue-light:#8cc3ee;
    --ink:#1a1f2b;
    --grey:#5b6270;
    --white:#ffffff;
  }
  *{box-sizing:border-box;margin:0;padding:0}
  html,body{width:1200px;height:1000px;overflow:hidden}
  body{background:var(--page);position:relative;font-family:"Roboto",Arial,sans-serif;color:var(--ink)}
  .hanger{position:absolute;top:68px;width:350px;height:872px;background:var(--white);overflow:hidden;box-shadow:0 6px 18px rgba(0,0,0,.18)}
  .hanger--front{left:250px}
  .hanger--back{left:615px}
  .abs{position:absolute;line-height:1.15}
  .hole{position:absolute;border-radius:50%;background:var(--page)}

  /* front */
  .front-sky{left:0;top:0;width:350px;height:440px;background:linear-gradient(180deg,var(--blue-deep) 0%,var(--blue) 50%,#0d6fd0 100%)}
  .headline{font-family:"Montserrat",sans-serif;color:var(--white);font-weight:800;line-height:1}
  .headline__awe{left:58px;top:223px;font-size:44px;letter-spacing:-.5px}
  .headline__and{left:180px;top:226px;font-size:20px;font-weight:600}
  .headline__some{left:178px;top:251px;font-size:44px}
  .photo{left:0;width:350px}
  .photo--front{top:292px;height:200px;background:linear-gradient(180deg,#1b3d78 0%,#6b5e57 35%,#8a7868 55%,#4f7a3b 82%,#6a9a48 100%)}
  .photo--back{top:0;height:430px;background:linear-gradient(180deg,#bfc0dc 0%,#e8dbe2 30%,#eef0f2 55%,#c6ccd3 72%,#7e9a66 90%,#6d8f55 100%)}
  .wave{left:0;width:350px;height:80px}
  .wave--front{top:430px}
  .wave--back{top:360px}

  .offer-lead{left:0;width:350px;top:516px;text-align:center;font-family:"Montserrat",sans-serif;font-weight:700;font-size:17px;padding-left:30px}
  .offer-pct{left:46px;top:528px;font-family:"Montserrat",sans-serif;font-weight:800;font-size:40px;line-height:1;color:var(--blue)}
  .offer-detail{left:142px;top:535px;font-size:12.5px;line-height:1.1;font-weight:500}
  .offer-detail strong{color:var(--blue);font-weight:700}
  .savings-pill{left:44px;top:589px;width:262px;height:34px;border-radius:5px;background:var(--blue);color:var(--white);font-family:"Montserrat",sans-serif;font-weight:800;font-size:19px;text-align:center;line-height:34px}
  .package{left:40px;top:628px;width:270px;text-align:center;font-size:14px;font-weight:500;line-height:1.2}
  .package strong{color:var(--blue);font-weight:700}
  .package em{font-weight:700}
  .saving-you{left:0;top:664px;width:350px;text-align:center;color:var(--blue);font-family:"Montserrat",sans-serif;font-weight:800;font-size:17px;line-height:1}
  .agent-photo{left:28px;top:694px;width:125px;height:156px;border:4px solid var(--white);background:linear-gradient(180deg,#5a4a44 0%,#8e6d5b 45%,#2e3b5c 100%);box-shadow:0 2px 6px rgba(0,0,0,.25);z-index:2}
  .agent-name{left:163px;top:708px;font-family:"Great Vibes",cursive;font-size:26px;line-height:1}
  .agent-creds{left:163px;top:738px;font-size:10px;line-height:1.35;font-weight:500}
  .brand{font-family:"Montserrat",sans-serif;font-weight:700;color:var(--blue-deep);line-height:1}
  .brand--front{left:163px;top:778px;font-size:15px}
  .band-strip{left:0;width:350px;height:8px;background:var(--blue-light)}
  .band{left:0;width:350px;background:var(--blue)}
  .band-strip--front{top:804px}
  .band--front{top:812px;height:60px}
  .contact{color:var(--white);font-weight:700;font-size:12.5px;line-height:1.45}
  .contact--front{left:163px;top:826px}

  /* back */
  .benefits{left:14px;top:437px;width:322px;list-style:none;font-size:11px;line-height:1.2}
  .benefits li{position:relative;padding-left:16px;margin-bottom:8px}
  .benefits svg{position:absolute;left:0;top:1px}
  .example-pill{left:99px;top:600px;width:152px;height:20px;border-radius:3px;background:var(--blue);color:var(--white);text-align:center;font-family:"Montserrat",sans-serif;font-weight:600;font-size:13px;line-height:20px;z-index:2}
  .example-box{left:40px;top:612px;width:270px;height:36px;border:2px solid var(--blue-deep);padding-top:5px;text-align:center;font-family:"Montserrat",sans-serif;font-weight:600;font-size:12.5px;line-height:1.2}
  .example-box strong{color:var(--blue);font-weight:800}
  .example-note{left:180px;top:651px;width:130px;text-align:right;font-size:6.5px;font-style:italic;color:var(--grey)}
  .quote-mark{left:22px;top:672px;font-family:Georgia,serif;font-size:40px;color:#b8bec8;line-height:1}
  .quote{left:38px;top:682px;width:274px;text-align:center;font-style:italic;font-size:11.5px;line-height:1.2}
  .signature{left:0;width:318px;top:735px;text-align:right;font-family:"Great Vibes",cursive;font-size:17px;line-height:1}
  .signature-creds{left:0;width:318px;top:752px;text-align:right;font-size:6px;color:var(--grey);line-height:1}
  .fine-print{left:30px;top:762px;width:290px;text-align:center;font-size:6.5px;font-style:italic;line-height:1.25}
  .band-strip--back{top:782px}
  .band--back{top:790px;height:82px}
  .brand--back{left:28px;top:818px;color:var(--white);font-size:13px}
  .contact--back{left:140px;top:806px;font-size:12.5px}
</style>
</head>
<body>

<section class="hanger hanger--front">
  <div class="abs front-sky"></div>
  <div class="hole" style="left:143px;top:102px;width:100px;height:100px"></div>
  <div class="abs headline headline__awe">AWE</div>
  <div class="abs headline headline__and">and then</div>
  <div class="abs headline headline__some">SOME</div>
  <div class="abs photo photo--front" role="img" aria-label="Brick new-construction home at dusk with landscaped front yard"></div>
  <svg class="abs wave wave--front" viewBox="0 0 350 80" preserveAspectRatio="none">
    <path d="M0 42 C120 0 230 -6 350 12 L350 30 C230 14 120 22 0 62 Z" fill="#8cc3ee"/>
    <path d="M0 52 C120 12 230 6 350 22 L350 30 C230 14 120 22 0 62 Z" fill="#0a5cc0"/>
    <path d="M0 62 C120 22 230 14 350 30 L350 80 L0 80 Z" fill="#ffffff"/>
  </svg>

  <p class="abs offer-lead">Receive a minimum of</p>
  <p class="abs offer-pct">2.5%</p>
  <p class="abs offer-detail">or more to put<br>towards your<br><strong>NEW CONSTRUCTION</strong> home!</p>
  <p class="abs savings-pill">Maximize Your Savings!</p>
  <p class="abs package">My <em>Buy &amp; List</em> package offers a <strong>FLAT FEE</strong> on the sale of your current home.</p>
  <p class="abs saving-you">SAVING YOU</p>

  <div class="abs band-strip band-strip--front"></div>
  <div class="abs band band--front"></div>
  <div class="abs agent-photo" role="img" aria-label="Portrait of the agent"></div>
  <p class="abs agent-name">Dana Whitford</p>
  <p class="abs agent-creds">REALTOR®,<br>CRS, ABR, CNHS, CHMS</p>
  <p class="abs brand brand--front">Marston Pryce</p>
  <p class="abs contact contact--front">555.014.2290<br>danawhitford@mailbox.com</p>
</section>

<section class="hanger hanger--back">
  <div class="abs photo photo--back" role="img" aria-label="White two-storey new-construction home at sunset with front walkway"></div>
  <div class="hole" style="left:95px;top:98px;width:96px;height:96px"></div>
  <svg class="abs wave wave--back" viewBox="0 0 350 80" preserveAspectRatio="none">
    <path d="M0 48 C130 36 240 10 350 0 L350 20 C240 28 130 54 0 66 Z" fill="#8cc3ee"/>
    <path d="M0 58 C130 46 240 20 350 10 L350 20 C240 28 130 54 0 66 Z" fill="#0a5cc0"/>
    <path d="M0 66 C130 54 240 28 350 20 L350 80 L0 80 Z" fill="#ffffff"/>
  </svg>

  <ul class="abs benefits">
    <li><svg width="11" height="11" viewBox="0 0 11 11"><rect x=".5" y=".5" width="10" height="10" fill="none" stroke="#0a5cc0"/><path d="M2 5.5 L4.5 8 L9.5 1.5" fill="none" stroke="#0a5cc0" stroke-width="1.8"/></svg>We work with 100's of builders in the local area so you are not limited to a few "select" builders.</li>
    <li><svg width="11" height="11" viewBox="0 0 11 11"><rect x=".5" y=".5" width="10" height="10" fill="none" stroke="#0a5cc0"/><path d="M2 5.5 L4.5 8 L9.5 1.5" fill="none" stroke="#0a5cc0" stroke-width="1.8"/></svg>Homebuilders have the same bottom line sales price whether you have a REALTOR® representing you or not.</li>
    <li><svg width="11" height="11" viewBox="0 0 11 11"><rect x=".5" y=".5" width="10" height="10" fill="none" stroke="#0a5cc0"/><path d="M2 5.5 L4.5 8 L9.5 1.5" fill="none" stroke="#0a5cc0" stroke-width="1.8"/></svg>Rebate program will not affect the price you pay for your home. Brokerage fees are paid through a separate marketing fund, not from the sales price of your home.</li>
    <li><svg width="11" height="11" viewBox="0 0 11 11"><rect x=".5" y=".5" width="10" height="10" fill="none" stroke="#0a5cc0"/><path d="M2 5.5 L4.5 8 L9.5 1.5" fill="none" stroke="#0a5cc0" stroke-width="1.8"/></svg>Rebate program is in ADDITION to any builder or lender incentives.</li>
  </ul>

  <p class="abs example-pill">For Example:</p>
  <div class="abs example-box">
    <p>$400,000 equals a <strong>$10,000</strong> rebate!</p>
    <p>$500,000 equals a <strong>$12,500</strong> rebate!</p>
  </div>
  <p class="abs example-note">*Lender approval required</p>

  <span class="abs quote-mark">“</span>
  <p class="abs quote">I've sold hundreds of homes in the North Dallas area over the last 13 years, specializing in new construction homes. I would love to help you make your new home dreams a reality.</p>
  <p class="abs signature">Dana Whitford</p>
  <p class="abs signature-creds">REALTOR®, CRS, ABR, CNHS, CHMS</p>
  <p class="abs fine-print">Not intended to solicit homes already listed for sale or buyers already in a buyers agency agreement with another brokerage.</p>

  <div class="abs band-strip band-strip--back"></div>
  <div class="abs band band--back"></div>
  <p class="abs brand brand--back">Marston Pryce</p>
  <p class="abs contact contact--back">555.014.2290<br>danawhitford@mailbox.com</p>
</section>

</body>
</html>
```